Website design for an edge protection barrier system

- The design must be based around the attached HPID (home page information design) called CODE HPID. I've attached Word and PDF versions - these are the same. The table boxes are just for approximate placement of information – you DON'T have to make it look exactly like this. All fonts used in the HPID are only examples - you can use any Google font you wish.

- Information only is in orange text. Copy to go on the design in black text. Some instructions are in the HPID. Please be creative!

- The design needs to be modern. Colours are to be black and white with orange ...like the logo colours.

- I've provided the images for the galleries - they are labelled and will match the name in the HPID.

- Examples of some websites that have great design... don't copy them please but they are similar in look to what we are after....
http://wandertrail.co.nz/
http://www.lumfuel.co.nz/
http://www.tolbertwade.co.nz/

Width of content will be 1100 pixels when implemented as a web page. Header height (without nav bar) 150-160 pixels.

If your design is chosen the winning PSD file will have to be provided as follows…
1. Canvas size of 2000px x 2000px - 72ppi in Adobe Photoshop (CS5 compatible)
2. Width of content section is 1100px wide - centered in the canvas
3. Any button rollovers/hovers in the PSD as hidden layers.
4. All fonts used must be Google fonts (except for the fonts in the header at the top of the page).
5. You will need to supply the chosen home page plus one example page (example page as a style guide for how all other pages will look). Example page is only the header and navigational bar at the top, an empty sector in the middle with a column (180 px wide) which can be left or right aligned which means the main sector is 920 pixels wide, and then the footer at the bottom of the page
Updates

Hi all, As per the HPID for the main image gallery you must use: File 7: edge protection systems for new houses hp wednesday, 17 december 2014 04:35:4112 AND File 9: R bracket for new home edge protection hp wednesday, 17 december 2014 04:35:4111 Use these images so they fit next to each other with the words: Edge protection systems for new houses with timber or aluminium rails (These words must be used either on or above or below the gallery) What we are looking for is a clean modern layout of the home page. The images supplied must be used please. Thank you.

Our office is closed over the New Year holiday season so decisions on designs may be delayed.

```html
<!DOCTYPE html>
<html lang="en">
<head>
<meta charset="utf-8">
<title>Rimguard NZ Ltd – Edge Protection Systems</title>
<link rel="stylesheet" href="https://fonts.googleapis.com/css2?family=Source+Sans+Pro:ital,wght@0,400;0,600;0,700;1,400;1,600&family=Didact+Gothic&display=swap">
<style>
:root{
  --black:#0d0c0b;
  --dark:#171615;
  --warm-dark:#221e19;
  --orange:#f0a21e;
  --hero-orange:#f2a81f;
  --footer-orange:#c8870f;
  --text-light:#f1ece3;
  --nav-text:#1d1d1d;
  --rule:#4a463f;
  --divider:#8e5f0a;
}
*{box-sizing:border-box;margin:0;padding:0}
html,body{width:1200px;height:2198px;overflow:hidden;background:var(--black)}
body{font-family:"Source Sans Pro",Arial,sans-serif;color:var(--text-light);position:relative}
.header{position:absolute;left:0;top:0;width:1200px;height:132px;background:var(--black)}
.brand{position:absolute;left:104px;top:36px;display:flex;align-items:center;gap:14px}
.brand-mark{width:34px;height:34px;background:var(--orange);border-radius:50%}
.brand-name{font-size:40px;font-weight:600;color:var(--text-light);line-height:1}
.tagline{position:absolute;right:100px;top:30px;color:var(--orange);font-size:19px;font-weight:600}
.phone{position:absolute;right:100px;top:66px;color:#fff;font-size:25px;font-weight:600}
.nav{position:absolute;left:0;top:132px;width:1200px;height:49px;background:linear-gradient(#fafafa,#e4e4e4);display:flex;padding-left:100px}
.nav a{font-size:12px;font-weight:600;color:var(--nav-text);text-decoration:none;text-transform:uppercase;padding:0 15px;line-height:49px;border-right:1px solid #c9c9c9}
.nav a.active{border-bottom:3px solid #333}
.nav a:last-child{border-right:none}
.hero{position:absolute;left:0;top:181px;width:1200px;height:455px;background:linear-gradient(180deg,var(--hero-orange),#e39a18)}
.hero h1{position:absolute;left:0;width:1200px;top:128px;text-align:center;font-family:"Didact Gothic",Arial,sans-serif;font-weight:400;color:#111;font-size:45px;line-height:56px;-webkit-text-stroke:0.7px #111}
.systems{position:absolute;left:0;top:636px;width:1200px;height:894px;background:var(--dark)}
.card{position:absolute;width:288px}
.card h3{font-size:19px;font-weight:700;color:#fff;text-transform:uppercase;margin-bottom:10px;height:26px}
.card .shot{width:288px;height:118px;border:4px solid #e9e9e9}
.rule{position:absolute;left:100px;width:1000px;height:1px;background:var(--rule)}
.video{position:absolute;left:104px;top:1158px;width:457px;height:262px;background:linear-gradient(135deg,#f5f5f5,#dcdcdc)}
.video .play{position:absolute;left:154px;top:45px}
.video .bar{position:absolute;left:0;bottom:0;width:100%;height:30px;background:#1f1f1f}
.video-caption{position:absolute;left:104px;top:1432px;width:500px;color:var(--orange);font-size:23px;font-weight:600;line-height:30px}
.intro{position:absolute;left:603px;top:1168px;width:470px}
.intro h2{color:var(--orange);font-size:30px;font-weight:600;margin-bottom:22px}
.intro p{font-size:14.5px;line-height:22px;color:#eee;margin-bottom:22px}
.btn{position:absolute;left:916px;top:1427px;width:152px;height:41px;border-radius:8px;background:linear-gradient(#f6b132,#d98d10);color:#fff;font-size:20px;font-weight:600;text-align:center;line-height:41px}
.testimonial{position:absolute;left:0;top:1531px;width:1200px;height:398px;background:var(--warm-dark)}
.testimonial .shot{position:absolute;left:106px;top:65px;width:352px;height:242px}
.quote{position:absolute;left:480px;top:74px;width:610px}
.quote h2{color:var(--orange);font-size:25px;font-weight:600;line-height:30px;margin-bottom:16px}
.quote p{font-size:13.5px;line-height:21px;color:#eee}
.quote .cite{text-align:right;color:var(--orange);font-style:italic;font-weight:600;font-size:14px;line-height:20px;margin-top:14px}
.footer{position:absolute;left:0;top:1929px;width:1200px;height:269px;background:var(--footer-orange);color:#fff}
.fcol{position:absolute;top:30px}
.fcol h4{font-size:17px;font-weight:700;color:#111;margin-bottom:22px}
.fcol li{list-style:none;font-size:14px;line-height:20px}
.fcol p{font-size:14px;line-height:20px}
.fphone{margin-top:8px;color:#fff}
.fdiv{position:absolute;top:20px;width:4px;height:230px;background:var(--divider)}
.made{font-style:italic;font-weight:600;color:#111;font-size:13px;margin-top:14px}
</style>
</head>
<body>
<header class="header">
  <div class="brand"><span class="brand-mark"></span><span class="brand-name">Rimguard</span></div>
  <div class="tagline">Innovative edge protection system for the building industry - NZ wide</div>
  <div class="phone">0800 RIMGRD | 0800 746473</div>
</header>
<nav class="nav">
  <a class="active">Home</a><a>About Us</a><a>Edge Protection Systems</a><a>Safety</a><a>Testimonials</a><a>Gallery</a><a>Downloads/Videos</a><a>Quote / Contact</a>
</nav>
<section class="hero" role="img" aria-label="Photo of house framing with edge protection rails, tinted orange">
  <h1>Edge protection systems<br>for new houses with timber or aluminium rails</h1>
</section>
<section class="systems">
  <div class="card" style="left:108px;top:42px"><h3>New Build Soffit Mount…</h3><div class="shot" role="img" aria-label="Photo of soffit mount bracket" style="background:linear-gradient(135deg,#e4a52a,#6b7f86)"></div></div>
  <div class="card" style="left:462px;top:42px"><h3>New Build Truss Mount…</h3><div class="shot" role="img" aria-label="Photo of truss mount bracket" style="background:linear-gradient(135deg,#d7cfc0,#e8a526)"></div></div>
  <div class="card" style="left:812px;top:42px"><h3>Re-roof…</h3><div class="shot" role="img" aria-label="Photo of re-roof bracket" style="background:linear-gradient(135deg,#6b3a25,#b5bcc4)"></div></div>
  <div class="card" style="left:108px;top:235px"><h3>New Build Soffit Mount…</h3><div class="shot" role="img" aria-label="Photo of house with soffit mount rails" style="background:linear-gradient(180deg,#3f78c6,#cfd3d6)"></div></div>
  <div class="card" style="left:462px;top:235px"><h3>New Build Truss Mount…</h3><div class="shot" role="img" aria-label="Photo of timber frame house with truss mount rails" style="background:linear-gradient(180deg,#c6c6c4,#9c8153)"></div></div>
  <div class="card" style="left:812px;top:235px"><h3>Re-roof…</h3><div class="shot" role="img" aria-label="Photo of re-roof bracket close up" style="background:linear-gradient(135deg,#e49b24,#c7d2d8)"></div></div>
</section>
<div class="rule" style="top:1083px"></div>
<div class="video" role="img" aria-label="Video player showing an animated bracket">
  <svg class="play" width="150" height="150" viewBox="0 0 150 150"><circle cx="75" cy="75" r="72" fill="#d0d0d0" fill-opacity=".85"/><path d="M58 45 L108 75 L58 105 Z" fill="#111"/></svg>
  <div class="bar"><svg width="457" height="30" viewBox="0 0 457 30"><path d="M14 9 L22 15 L14 21Z" fill="#fff"/><rect x="40" y="14" width="300" height="3" fill="#777"/><rect x="40" y="14" width="110" height="3" fill="#e9a32a"/><rect x="380" y="11" width="6" height="8" fill="#fff"/><path d="M386 11 L393 6 L393 24 L386 19Z" fill="#fff"/><rect x="405" y="14" width="20" height="3" fill="#fff"/><rect x="437" y="8" width="12" height="12" fill="none" stroke="#fff" stroke-width="2"/></svg></div>
</div>
<div class="video-caption">Watch the video on how the Edge Protection system works…</div>
<div class="intro">
  <h2>Edge Protection Systems…</h2>
  <p>Edge Protection is essential when working on buildings at height. Our systems are designed by experienced tradesmen and are manufactured in New Zealand.</p>
  <p>The R bracket is without a doubt the most versatile and cost effective Edge Protection on the market. The R Bracket system has been designed (and has passed stringent testing) to comply with AS/NZS 39931:2009.</p>
</div>
<div class="btn">LEARN MORE</div>
<div class="rule" style="top:1530px"></div>
<section class="testimonial">
  <div class="shot" role="img" aria-label="Photo of builders standing in front of a framed house with edge rails" style="background:linear-gradient(180deg,#c9c9c7 0%,#b08d57 60%,#5b7a3b 100%)"></div>
  <div class="quote">
    <h2>"I would recommend Rimguard NZ Ltd. to any<br>&nbsp;prospective purchaser"</h2>
    <p>"Corvale Homes Ltd. has used the services of Owen Hartley and his Rimguard Edge Protection. I was impressed both with the quality of the Edge Protection Owen Supplied and his knowledge and understanding of the new requirements being enforced by the Labour Dept. I had a meeting with the Labour Dept. representative in my office which Owen attended and Owen introduced a simple and easy way to address the issue which was more than the Labour Dept. were prepared to offer. I would recommend Rimguard N.Z. Ltd. to any prospective purchaser."</p>
    <div class="cite">Maria Teller.<br>Director of Corvale Homes Ltd</div>
  </div>
</section>
<footer class="footer">
  <div class="fcol" style="left:110px"><h4>Fotter Links</h4><ul><li>Home</li><li>About Us</li><li>Safety</li><li>Testimonials</li><li>Gallery</li><li>Downloads/Videos</li><li>Quote / Contact</li></ul><p class="fphone">0800 RIMGRD | 0800 746473</p></div>
  <div class="fdiv" style="left:324px"></div>
  <div class="fcol" style="left:390px"><h4>Edge Protection Systems</h4><ul><li>New Build Soffit Mount</li><li>New Build Truss Mount</li><li>Re-roof</li><li>Garage and Sheds</li><li>Commercial – coming soon</li><li>New product – coming soon</li></ul></div>
  <div class="fdiv" style="left:662px"></div>
  <div class="fcol" style="left:708px;width:380px"><h4>Patent. 581936 Design Registration. 402278</h4><p>Important: All our systems are the property of Rimguard New Zealand Ltd. It is company policy to vigorously prosecute any attempts to copy our innovations and designs.</p><p class="made">Proudly New Zealand Made</p></div>
</footer>
</body>
</html>
```